Flyer für Installationsfirma für hochwertige Multimedia- und Beschallungslösungen, insbesonder in Kirchen und öffentlichen Bereichen mit Menschenansammlungen
Zielgruppe
Wir sind eine Installationsfirma für hochwertige Multimedia- und Beschallungslösungen in akustisch schwierigen Räumen. Im weiteren auch der Umbau auf LED Leuchten und dazugehörende Steuerungen. Unser Geschäft ist in Festinstallationen und Rentalbereich 'unterteilt' Weitere Infos auch auf www. brando-vex.ch
Unser Zielpublikum sind die Festinstallation für Kirchen und öffentliche Räume. Mehrzweckräume, Bühnen, Kirchen, Aulas, Bahnhofshallen, Warteräume, Konferenzräume, Tagungszentren usw. Bei diesem Flyer sollen speziell die Kirchen beworben werden. Es ist wichtig dass nebst den oben beschriebenen Leistungen auch die Displaylösung für Liedanzeigen hervorgehoben wird.
Aufgabenstellung
Ansprechender Werbe-Flyer A4 2 Seitig
Spezifische Bilder und Texte zu den versch. Angebotsbereichen für Kirchen im Anhang. Vorschläge des Grafikers sind willkommen !
Die Texte und Bilder sollten von uns angepasst und korrigiert werden können !

```html
<!DOCTYPE html>
<html lang="de">
<head>
<meta charset="utf-8">
<title>Brandovex Flyer</title>
<link href="https://fonts.googleapis.com/css2?family=Poppins:wght@500;700&family=Open+Sans:wght@400;600;700&family=Roboto:wght@500&display=swap" rel="stylesheet">
<style>
:root{
  --bg:#e9e8ea;
  --navy:#16223a;
  --navy-deep:#111a2d;
  --band:#1f3b5c;
  --accent:#2a9ad8;
  --white:#ffffff;
  --muted:#c9d0dc;
  --photo-warm:#d9cfc4;
  --photo-mid:#8d7e6f;
}
*{box-sizing:border-box;margin:0;padding:0}
html,body{width:909px;height:1200px;overflow:hidden;background:var(--bg)}
body{position:relative;font-family:"Open Sans",sans-serif}
.page{position:absolute;top:303px;width:420px;height:594px;background:var(--navy);overflow:hidden;box-shadow:0 6px 18px rgba(0,0,0,.25)}
.page--front{left:20px}
.page--back{left:469px}
.abs{position:absolute}

/* front */
.hero-photo{left:0;top:0;width:420px;height:330px;
  background:linear-gradient(180deg,var(--photo-warm) 0%,#e6ddd2 35%,var(--photo-mid) 55%,#5b5650 68%,rgba(22,34,58,0) 100%)}
.hero-fade{left:0;top:140px;width:420px;height:200px;background:linear-gradient(180deg,rgba(22,34,58,0) 0%,var(--navy) 100%)}
.brand-mark{left:36px;top:30px;display:flex;align-items:center;gap:6px}
.brand-mark .dot{width:14px;height:14px;border-radius:50%;background:#2b2a28}
.brand-mark .name{font-family:"Poppins",sans-serif;font-weight:500;font-size:13px;color:#2b2a28;letter-spacing:.5px}
.headline{left:0;top:225px;width:420px;text-align:center;font-family:"Poppins",sans-serif;font-weight:700;font-size:24.5px;line-height:30px;color:var(--white);letter-spacing:.3px}
.headline .hl{color:var(--accent)}
.intro{left:28px;top:333px;width:364px;text-align:center;font-size:7px;line-height:11.9px;color:var(--muted)}
.features{left:18px;top:422px;width:384px;display:flex;justify-content:space-between}
.feature{width:92px;text-align:center;color:var(--white)}
.feature svg{width:40px;height:48px;display:block;margin:0 auto 8px}
.feature p{font-family:"Roboto",sans-serif;font-weight:500;font-size:12px;line-height:15px}
.footer{left:0;bottom:0;width:420px;height:56px;background:var(--band);display:flex;align-items:center;padding-left:34px;gap:20px}
.footer .name{font-family:"Poppins",sans-serif;font-weight:500;font-size:20px;color:var(--white);letter-spacing:1px}
.footer .contact{font-size:8px;line-height:14px;font-weight:700;color:var(--white)}

/* back */
.page--back .footer{height:66px;padding-left:34px}
.services-title{left:0;top:30px;width:431px;width:420px;text-align:center;font-family:"Poppins",sans-serif;font-weight:700;font-size:25px;color:var(--white);text-shadow:0 0 18px rgba(42,154,216,.6)}
.services-title .hl{color:var(--accent)}
.service-photo{width:108px;height:72px;border:2px solid #d8d8d8}
.photo-speaker{background:linear-gradient(135deg,#a38e6f,#d3c6b3 60%,#7c6b58)}
.photo-nave{background:linear-gradient(180deg,#d6c6a8,#b38d5e 55%,#4b3a2a)}
.photo-rack{background:linear-gradient(160deg,#3a3d3a,#1c1f1c 50%,#5a6f3e)}
.photo-display{background:linear-gradient(180deg,#5b7f3c,#7da24c 50%,#3b2f2a)}
.service-head{font-family:"Poppins",sans-serif;font-weight:700;font-size:11.5px;color:var(--white)}
.service-head .hl{color:var(--accent)}
.service-text{font-size:7px;line-height:11.9px;color:var(--muted)}
.cta{left:57px;top:466px;width:300px;height:47px;border:1.5px solid var(--accent);display:flex;align-items:center;justify-content:center;text-align:center;font-weight:700;font-size:9px;line-height:14px;color:var(--white)}
</style>
</head>
<body>

<section class="page page--front">
  <div class="abs hero-photo" role="img" aria-label="Foto eines hellen barocken Kirchenschiffs mit Bankreihen und Altar"></div>
  <div class="abs hero-fade"></div>
  <div class="abs brand-mark"><span class="dot"></span><span class="name">BRANDOVEX</span></div>
  <h1 class="abs headline">ZEITGEMÄSSE<br>MEDIENINSTALLATION<br><span class="hl">FÜR KIRCHENRÄUME</span></h1>
  <p class="abs intro">Multimediainstallation in Kirchen und EventräumenFür heutige Gottesdienste und multifunktionellen Betrieb von Gotteshäusern wird eine moderne Medientechnik benötigt. Beschallungssysteme mit sehr guter Sprachverständlichkeit durch Beam-Steering Technologie und dezenter Optik, LED-Beleuchtung und Projektion sind selbstverständlich geworden. Gleichzeitig gehört eine Integration der Heizung und Glockensteuerung zusammen mit der AV-Installation und einfache Bedienung via Tablet zum heutigen Anforderungsprofil einer Kirche.</p>
  <div class="abs features">
    <div class="feature">
      <svg viewBox="0 0 40 48" fill="none" stroke="#fff" stroke-width="1.5"><circle cx="20" cy="18" r="15"/><circle cx="20" cy="18" r="11"/><path d="M11 30l-2 14 6-4 3 5M29 30l2 14-6-4-3 5"/><text x="20" y="20" font-size="7" fill="#fff" stroke="none" text-anchor="middle" font-family="Roboto,sans-serif">25</text></svg>
      <p>25 Jahre<br>Erfahrung</p>
    </div>
    <div class="feature">
      <svg viewBox="0 0 40 48" fill="none" stroke="#fff" stroke-width="1.5"><circle cx="20" cy="18" r="15"/><circle cx="20" cy="18" r="10"/><path d="M20 12l2 4.5 4.5.4-3.4 3 1 4.5-4.1-2.4-4.1 2.4 1-4.5-3.4-3 4.5-.4z"/><path d="M11 30l-3 14 6-3 3 5M29 30l3 14-6-3-3 5"/></svg>
      <p>Hochwertige<br>Ausrüstung</p>
    </div>
    <div class="feature">
      <svg viewBox="0 0 40 48" fill="none" stroke="#fff" stroke-width="1.5"><path d="M20 26c-6-4-9-7-9-11a4.5 4.5 0 0 1 9-1 4.5 4.5 0 0 1 9 1c0 4-3 7-9 11z"/><path d="M5 36h8l6 3h9c2 0 2-3 0-3h-7M13 36l9-4 10 2"/><path d="M20 2v4M8 6l2 3M32 6l-2 3M3 16h4M33 16h4"/></svg>
      <p>Umfassender<br>Service</p>
    </div>
    <div class="feature">
      <svg viewBox="0 0 40 48" fill="none" stroke="#fff" stroke-width="1.5"><circle cx="11" cy="20" r="5"/><circle cx="29" cy="20" r="5"/><circle cx="20" cy="14" r="6"/><path d="M2 42v-7a9 9 0 0 1 9-9M38 42v-7a9 9 0 0 0-9-9M10 44v-9a10 10 0 0 1 20 0v9"/></svg>
      <p>engagiertes<br>Team</p>
    </div>
  </div>
  <footer class="abs footer">
    <span class="name">BRANDOVEX</span>
    <p class="contact">Birkenweg 14 | 6410 Goldau | 041 555 20 10<br>mail@brando-vex.ch | www.brando-vex.ch</p>
  </footer>
</section>

<section class="page page--back">
  <h2 class="abs services-title">UNSERE <span class="hl">LEISTUNGEN</span></h2>

  <div class="abs service-photo photo-speaker" style="left:24px;top:82px" role="img" aria-label="Foto eines dezenten Säulenlautsprechers an einer Kirchenwand"></div>
  <h3 class="abs service-head" style="left:143px;top:80px"><span class="hl">BESCHALLUNG</span></h3>
  <p class="abs service-text" style="left:143px;top:98px;width:262px">Die Anforderungen in akustisch schwierigen Räumen sind sehr hoch. Neuartige Beschallungskonzepte mit Beam-Steering Technologie machen eine hohe Sprachverständlichkeit in Kirchenräumen mit langer Nachhallzeit möglich. Zusammen mit einer normgerechten Installation einer Gehörlosenschlaufe können alle am Gottesdienst teilnehmen.</p>

  <h3 class="abs service-head" style="left:24px;top:180px"><span class="hl">LED</span> BELEUCHTUNG</h3>
  <p class="abs service-text" style="left:24px;top:198px;width:246px">Eine neue stromsparende Beleuchtung ist für einen verantwortungsvollen Energieeinsatz unumgänglich. Die stromsparenden LED-Leuchten sind durch die sehr lange Lebensdauer wartungsfrei und sehr kosteneffizient. Moderne LED-Leuchtmittel sind zudem flickerfrei, dimmbar und in der richtigen Farbtemperatur erhältlich.</p>
  <div class="abs service-photo photo-nave" style="left:276px;top:183px" role="img" aria-label="Foto eines beleuchteten Kirchenraums mit vollen Bankreihen"></div>

  <div class="abs service-photo photo-rack" style="left:24px;top:280px" role="img" aria-label="Foto eines Technikracks mit Steuergeräten"></div>
  <h3 class="abs service-head" style="left:143px;top:282px"><span class="hl">INTERGRATION</span>/STEUERUNG</h3>
  <p class="abs service-text" style="left:143px;top:300px;width:262px">Beleuchtung, Beschallung, Projektion, Liedanzeige, Glockensteuerung und Friedhofsbeleuchtung. Viele Systeme zusammengeführt in eine übersichtliche und erweiterbare Steuerung über Netzwerk.</p>

  <h3 class="abs service-head" style="left:24px;top:377px"><span class="hl">LIEDER</span>/TEXTANZEIGEN</h3>
  <p class="abs service-text" style="left:24px;top:395px;width:250px">Kostengünstige Liedanzeigen mit 8 Zeilen in allen Farbkombinationen. Auch Bilder können angezeigt werden (z.B. für Beerdigungen /Hochzeiten/Taufen usw).</p>
  <div class="abs service-photo photo-display" style="left:276px;top:372px" role="img" aria-label="Foto einer grünen Liedanzeigetafel mit Elektronik"></div>

  <div class="abs cta">KONTAKTIEREN SIE UNS UNVERBINDLICH FÜR EIN<br>PERSÖNLICHES BERATUNGSGESPRÄCH.</div>

  <footer class="abs footer">
    <span class="name">BRANDOVEX</span>
    <p class="contact">Birkenweg 14 | 6410 Goldau | 041 555 20 10<br>mail@brando-vex.ch | www.brando-vex.ch</p>
  </footer>
</section>

</body>
</html>
```